Start Up Business Launcher needs a business card

We need a business card logo and word design for a new company called Varnquist Ventures. We are a company dedicated to creating, testing, and developing, a myriad of repeatable and scalable business models (start ups) through innovative and consistent application of knowledge and expertise.

Target Market(s)

We test the marketability of start ups to various clientelle

Industry/Entity Type

Startup

Contact Information for Business Card

Varnquist Ventures
Milo Hartwin LL.B, MBA.
Founder and President
#402 118 27 Ave NE Calgary AB
varnquistventures@mailbox-demo.net
(403) 555-0193

Colors

Designer to choose colors to be used in the design.

Requirements
Must have
• A logo for Varnquist Ventures and a stylized written logo for Varnquist Ventures
Nice to have
• bold design that demonstrates professionalism, consistency, and innovation.

```html
<!DOCTYPE html>
<html lang="en">
<head>
<meta charset="utf-8">
<title>Varnquist Ventures — Business Card</title>
<link rel="stylesheet" href="https://fonts.googleapis.com/css2?family=Chivo:ital,wght@0,400;0,800;1,400&display=swap">
<style>
  :root {
    --page-bg: #ffffff;
    --card-dark: #3b393c;
    --card-light: #ffffff;
    --brand-yellow: #e9c300;
    --ink: #1e1e1e;
    --ink-soft: #333134;
    --white: #ffffff;
  }
  * { box-sizing: border-box; margin: 0; padding: 0; }
  html, body {
    width: 1200px;
    height: 1000px;
    overflow: hidden;
    background: var(--page-bg);
    font-family: "Chivo", Arial, sans-serif;
  }
  .canvas { position: relative; width: 1200px; height: 1000px; }

  .card {
    position: absolute;
    left: 256px;
    width: 685px;
    height: 391px;
    box-shadow: 0 2px 10px rgba(0, 0, 0, 0.12);
    overflow: hidden;
  }

  /* Front */
  .card-front { top: 83px; background: var(--card-dark); }
  .card-front .brand-dot {
    position: absolute;
    left: 299px; top: 119px;
    width: 60px; height: 60px;
    border-radius: 50%;
    background: var(--brand-yellow);
  }
  .card-front .brand-name {
    position: absolute;
    left: 0; right: 0; top: 218px;
    text-align: center;
    font-size: 38px;
    font-weight: 400;
    color: var(--white);
    letter-spacing: 0.2px;
  }

  /* Back */
  .card-back { top: 508px; background: var(--card-light); }
  .card-back .brand-dot {
    position: absolute;
    left: 453px; top: 38px;
    width: 50px; height: 50px;
    border-radius: 50%;
    background: var(--brand-yellow);
  }
  .card-back .brand-name {
    position: absolute;
    right: 64px; top: 103px;
    font-size: 27px;
    font-weight: 400;
    color: var(--ink-soft);
  }
  .contact-block {
    position: absolute;
    right: 64px; top: 193px;
    text-align: right;
    color: var(--ink);
  }
  .person-name { font-size: 22px; font-weight: 800; line-height: 28px; }
  .person-credentials { font-size: 17px; font-weight: 400; }
  .person-title { font-size: 20px; font-style: italic; line-height: 26px; }
  .contact-lines { margin-top: 20px; font-size: 21px; line-height: 26px; }
</style>
</head>
<body>
<main class="canvas">
  <section class="card card-front" aria-label="Card front">
    <span class="brand-dot" aria-hidden="true"></span>
    <p class="brand-name">Varnquist Ventures</p>
  </section>

  <section class="card card-back" aria-label="Card back">
    <span class="brand-dot" aria-hidden="true"></span>
    <p class="brand-name">Varnquist Ventures</p>
    <div class="contact-block">
      <p class="person-name">Milo Hartwin <span class="person-credentials">LL.B, MBA.</span></p>
      <p class="person-title">Founder and President</p>
      <div class="contact-lines">
        <p class="phone">(403) 555-0193</p>
        <p class="email">varnquistventures@mailbox-demo.net</p>
        <p class="address">#402 118 27 Ave NE Calgary AB</p>
      </div>
    </div>
  </section>
</main>
</body>
</html>
```